BendTheRoutine-fitness app follows the owner or client moves, let them monitor their weight & fitness

BendTheRoutine -fitness app, the avatar changes & evolve with the data logged in. the avatar resembles the client. the avatar weight looks like the client. When the client loses weight or gains weight, the avatar changes.
A brief is attached, check it out and get back to me with you're design.

Every week I will increase by 100€ instead.

Bendtheroutine -fitness App Idea.
Two Business Logo.

March 2013 Ireland, the land of magic. Bendtheroutine was born. Copy the client moves. With the avatar.
The app is about fitness, I have a vision and that you can be part of it.
Let's change the world together!
- the 1st page is about bendtheroutine mission/founder/value of the company.
I will attach all information on Page(A)
after the intro, Terms and conditions poly/data policy ( the client has to agree and Sign before continuing. Then comes the page ParQ
the ParQ is a questionnaire asking the client to know more about them!
ParQ features the beginning: Create your personalized Avatar ( change clothes – if they choose no cloths, by default the avatar will have a pair of short- pant/hair/ eyes colour/ and select Body type: Ectomorph/ endomorph/ mesomorph or the client can select a mix body type.
Age select/ currant weight/ desired weight/ skin colour/ gender: male, female, Transgender, other.
Fitness goals: what the client desire how they are going to achieve it/ the measure they will take to achieve it or I don’t know option. The press continues / the app analyses all the data and create their personalise unique Avatar. That will look like the description they provided.
Page 2nd feature: they will see their full-body avatar.
Next, the client needs to continue completing more information.
Stress level select/ nutrition habits select/ and nutrition habit desired select/ injuries select/ allergies select/ history of any health complication question to answer/ Gp ( their Doctor name and number, to fill in/ and a person to contact in case of an emergency. Fill-in answer).
Page 3rd The Main Page. This results will depend on the answer of E-Wallet (5)
BendTheRoutine-fitness Pro APP, Will analyse all the data and the app will suggest the best fitness program, nutrition plan, meditation advice to help them with stress/ and sleep hours they need to recover from after exercise/ base on their body type, fitness goal, and current stress level.
Main page Features: Keep in mind; the avatar changes form constantly, all depend on the information the client put on the profile setting.
1- the Avatar
- the can look Happy
- or sad – the reason why! Can tell the client all the reason for being that way and the solutions to make it better.
- Angry- Reason why! Can tell the client all the reason for being that way and the solutions to make it better.
- if the client gain weight, it will show on the avatar body.
- When the client loses weight the avatar will tell the client with a notification and it shows o the avatar body.
2- fitness check the app call Brawnly and Sunny Limbs fitness app, I like their page layout, it might show you what type of page I’m looking for and the quality that hoping or expecting.
- Muscle 3d full body when selecting a muscle it will show you the best exercises to work that particular muscle and weight recommendation. Check the app called
- Fitness Equipment to target each muscle and best suggestion for each muscle.
- Exercises all exercise available to get someone I top shape and the option to add more custom exercises. Liked exercise option/ search for exercises option/ reminder option.
- Nutrition Plans ( Vegan option/ paleo diet Option/ Keto diet/ build their own pers meal plan.
- Wellness Suggestions, tips raising your energy level
3- social Media
- Snapgrove
- ChirpLine
- Boardnook
- Meetwall
Feedback option
4- Music
- connect to Tunedrift.
- Connect to playlist Custom
- Connect to Wavelark
5- E-wallet
- buy a 1to1 personal training session ( only for members living in the country as
the founder)
- Buy 1 sessions/ 45Minutes 45€
- Buy 1sessions / 30 Minutes 35€
- Buy 1 session / 60 Minutes 55€
App subscription ( 2 options)
- Buy one Month subscription 7.99€ app
- Buy one Year Subscription for 107.88€ Share it with 10 people for the best deal 49.99€ for 12 months.
6- share it
on any social platform on the list
7- Picture Gallery
- before Pic
- after pic
8 – Deals & Offers
link to affiliated with other organization( bendtheroutine will put all fitness deals and offers on this page.
9 –Contacts
- Gps number and information
-- Friend or family to contact during an emergency
10- Testimonials
- Reviews
11- To-do List
- Calendar bookings
- fitness goal planner
12- Chat On The app community
- a page where all the app members can chat if they open the portal and agree to it.
13- Profile settings
- account settings
14-Progress Tracker
15 – Connect Fit Device
-- Progression CHART.
- Junk food / sweet tracker (obviously the client need to log in what they eat each time.
Base on what they eat the Avatar will take shape/ increase weight or lose weight / change mood/ the client will know when they are doing something wrong or right base on how the avatar mood.
I this idea is yours to be part of something different, this idea is will donate for young and family who need help and support.

WELCOME TO BendTheRoutine-fitness Private Studio
OUR MISSION
BendTheRoutine an Ireland based company whose mission is to help you
complete your journey stronger, faster with confidence.
ABOUT BENDTHEROUTINE
BendTheRoutine-fitness Was created from and inspire by the Irish strength and power to conquer any challenges, in 2013 after winning a boxing tournament in the national stadium. Driven by the desire to make a difference in the sports industry, I won that knight because my hunger for success was bigger than my opponents. BendTheRoutine-fitness Private Studio, I decided to teach and coach people, how to improve their fitness components with all the experience I have under my belt. My Mission is to inspire and be inspired by the new young talents in need for an opportunity.
BendTheRoutine-fitness Private Studio – Your energy is what keeps us moving and striving for a better and stronger united community. Fitness is the future & wellness is life.
I. OUR FOUNDER
Born and raised in the Caribbean, I started boxing when I was 19 years of age.
I started fighting to learn how to defend myself from bullying and protect my mother.
I started winning all my amateur fights, travelling around the world, the idea of travelling and the famous side of being a fighter kind started to like a little bit. My ambition didn’t stop there, it grew to aim for the stars and bigger plans.
I always dreamed of owning my own cloth brand and my own fitness gym. All over the Caribbean.
My peaceful Land (Dominican Rep, gave me the qualities to rise and achieve many goals. I believe- everything and anything is possible, once you have the right mindset and dedication to achieve it.
Trained by many of the best in coach in Ireland.
Now is time to share my knowledge.
OUR VALUES:
We value top quality Service and will ensure you have an amazing experience with BendTheRoutine Fitness. If not, write to us and we’ll make it right.
II. GIVING BACK:
To help and support those in need in our communities.
10% of our earning will be used to help and support people in need in the Dominican Republic, Haiti and all the Caribbean. We support our young athletes with big dreams. Seeing them succeed is the best gift the world can give us all.
Good Luck to all who will take this challenge. Remember this is only the start, the winner will gain an extra bonus for completing this work. And the chance to continue working with us.
III. You Can check the app call fitness Ally or sunny limbs a fitness app
these fitness features and setting is the style and standard I am looking for.

Target Market(s)

Fitness/ Nutrition & well Being

Contact Information for Business Card

Bendtheroutine@quillpost.example
0871427706
www.bendtheroutinefitness.example
The logo is on my brief.
On the card, I want bendTheRoutine Fitness Pro.
I like an attractive colour like gold champagne on the main front side and on the back I want black and green to match the logo. sharp and professional style.

Font styles to use
Serif
Decorative
Script

Requirements
Must have
• Most have an option to create an avatar, to look like the client profile and weight/ hairstyle. This session is for the (App) https://vidshare.example/Qx83LmTpRaZ
Ectomorph body type.
Endomorph body type.
mesomorph body type.
or a mix body type option.
base on the body type the client will be suggested by the bendtheroutine the best plan for them.
Most have a challenges page: like squat challenge/ push-Ups challenge/ few fitness challenges to motivate the client.
Nice to have
• I would like to have every single muscle on the human body with all the exercises to work that particular muscle. like fitness ally or sunny Limbs fitness app
Must have a progression chart, to show the client his/her fitness progression on their: strength/ speed/ push-ups/ flexibility/ Cardio or their V02 Max.
also, Fitness test option; every month or even every the client wishes the can test their fitness.

I found an Idea on the net: https://vidshare.example/Qx83LmTpRaZ
Thank you, a step closer to a better world.

```html
<!DOCTYPE html>
<html lang="en">
<head>
<meta charset="utf-8">
<title>BendTheRoutine Fitness – App Screens</title>
<link href="https://fonts.googleapis.com/css2?family=Fira+Sans:wght@400;500;600;700&family=Roboto:wght@400;500&display=swap" rel="stylesheet">
<style>
:root{
  --bg:#e7eff5;
  --green:#0cb31a;
  --green-dark:#079a14;
  --green-top:#0fbb1c;
  --green-mid:#2fd45a;
  --teal:#43ecb6;
  --card:#f3f5f9;
  --ink:#222629;
  --ink-soft:#3a3f44;
  --line:#dfe3e8;
  --star:#f5a623;
  --red:#e0262b;
  --button:#2b2c2c;
  --white:#ffffff;
}
*{box-sizing:border-box;margin:0;padding:0}
html,body{width:1200px;height:846px;overflow:hidden;background:var(--bg)}
body{font-family:"Roboto",sans-serif;color:var(--ink)}
.stage{position:absolute;left:0;top:0;width:1626px;height:1147px;transform:scale(0.738);transform-origin:0 0}
.screen{position:absolute;top:162px;width:371px;height:836px;border-radius:42px;overflow:hidden;
  background:linear-gradient(180deg,var(--green-top) 0%,var(--green-mid) 55%,var(--teal) 100%)}
.screen--todo{left:140px}
.screen--reviews{left:620px}
.screen--social{left:1100px}
.topbar{position:absolute;left:0;top:44px;width:100%;height:36px;color:var(--white);font-family:"Fira Sans",sans-serif}
.topbar__title{position:absolute;left:0;right:0;top:4px;text-align:center;font-size:21px;font-weight:500}
.topbar__back{position:absolute;left:18px;top:8px;display:flex;align-items:center;gap:8px;font-size:18px;font-weight:500}
.topbar__search{position:absolute;right:22px;top:8px}

/* To do list */
.plan-hero{position:absolute;left:17px;top:98px;width:333px;height:137px;
  background:linear-gradient(120deg,#6b6f73 0%,#3c3f42 50%,#1f2224 100%);color:var(--white);text-align:center;font-family:"Fira Sans",sans-serif}
.plan-hero__title{margin-top:40px;font-size:22px;font-weight:500}
.plan-hero__date{margin-top:4px;font-size:14px}
.calendar{position:absolute;left:17px;top:235px;width:333px;height:90px;background:var(--white);font-family:"Fira Sans",sans-serif;
  display:grid;grid-template-columns:54px 50px 42px 50px 52px 40px 45px;grid-template-rows:41px 49px}
.calendar span{display:flex;align-items:center;justify-content:center;border-right:1px solid var(--line)}
.calendar span:nth-child(7n){border-right:0}
.calendar .day{font-size:12px;color:var(--ink-soft);border-bottom:1px solid var(--line)}
.calendar .date{font-size:18px;color:var(--ink-soft)}
.calendar .date--today i{display:flex;align-items:center;justify-content:center;width:24px;height:24px;border-radius:50%;background:var(--red);color:var(--white);font-style:normal;font-size:16px}
.task{position:absolute;left:17px;width:333px;height:90px;background:var(--card)}
.task__photo{position:absolute;left:14px;top:17px;width:56px;height:56px;border-radius:50%;background:radial-gradient(circle at 40% 40%,#c9b2a2,#6a5a54)}
.task__title{position:absolute;left:87px;top:14px;font-size:16.5px;color:var(--ink)}
.task__sub{position:absolute;left:87px;top:37px;font-size:13px;color:var(--ink)}
.task__time{position:absolute;left:87px;top:61px;font-size:13.5px;color:var(--green);display:flex;align-items:center;gap:5px}
.task__go{position:absolute;right:17px;top:35px}

/* Testimonials */
.brand-name{position:absolute;left:0;right:0;top:114px;text-align:center;color:var(--white);font-family:"Fira Sans",sans-serif;font-size:17px;font-weight:500;letter-spacing:1px}
.review{position:absolute;left:19px;width:331px;height:162px;background:var(--card);border-radius:4px}
.review__photo{position:absolute;left:21px;top:25px;width:66px;height:66px;border-radius:50%;background:radial-gradient(circle at 45% 40%,#a88472,#2e2420)}
.review__head{position:absolute;left:107px;top:20px;display:flex;align-items:center;gap:8px;font-family:"Fira Sans",sans-serif}
.review__quote{font-size:34px;font-weight:700;line-height:1;height:22px;overflow:hidden;margin-top:-2px}
.review__name{font-size:17px;font-weight:500}
.review__stars{margin-left:14px;display:flex;gap:1px}
.review__text{position:absolute;left:109px;top:52px;width:214px;font-size:13.5px;line-height:18px;color:var(--ink)}
.more-reviews{position:absolute;left:18px;top:733px;width:333px;height:52px;background:var(--button);color:var(--white);
  font-family:"Fira Sans",sans-serif;font-weight:600;font-size:18px;letter-spacing:.5px;display:flex;align-items:center;justify-content:center}

/* Social */
.network{position:absolute;width:159px;height:144px;background:var(--white);text-align:center;font-family:"Fira Sans",sans-serif}
.network__dot{display:block;width:70px;height:70px;border-radius:50%;background:var(--green);margin:21px auto 0}
.network__name{display:block;margin-top:14px;font-size:16.5px;font-weight:500;color:var(--ink)}
.feed{position:absolute;left:25px;top:259px;width:327px;height:384px;background:var(--card)}
.feed::before{content:"";position:absolute;left:227px;top:-10px;border:10px solid transparent;border-top:0;border-bottom-color:var(--card)}
.post{position:absolute;left:0;width:100%;border-bottom:1px solid var(--line)}
.post__avatar{position:absolute;width:60px;height:60px;border-radius:50%;border:2px solid var(--white);background:radial-gradient(circle at 50% 40%,#d9c4b4,#6f7d8c)}
.post__name{position:absolute;font-family:"Fira Sans",sans-serif;font-size:16.5px;font-weight:500;color:var(--ink-soft)}
.post__text{position:absolute;font-size:15px;line-height:21px;color:var(--ink-soft)}
.feed__more{position:absolute;left:0;right:0;top:344px;text-align:center;color:var(--green);font-size:15px;text-decoration:underline}
</style>
</head>
<body>
<div class="stage">

  <!-- To do list screen -->
  <section class="screen screen--todo">
    <header class="topbar">
      <span class="topbar__back"><svg width="22" height="20" viewBox="0 0 22 20"><path d="M10 2 2 10l8 8M2 10h18" fill="none" stroke="#fff" stroke-width="4" stroke-linecap="round" stroke-linejoin="round"/></svg></span>
      <h1 class="topbar__title">To do List</h1>
      <span class="topbar__search"><svg width="20" height="20" viewBox="0 0 20 20"><circle cx="8" cy="8" r="6" fill="none" stroke="#fff" stroke-width="3"/><path d="m12.5 12.5 5 5" stroke="#fff" stroke-width="3.4" stroke-linecap="round"/></svg></span>
    </header>
    <div class="plan-hero" role="img" aria-label="Photo of a woman working out in a gym">
      <div class="plan-hero__title">Personal Plan</div>
      <div class="plan-hero__date">Today, June 4</div>
    </div>
    <div class="calendar">
      <span class="day">SUN</span><span class="day">MON</span><span class="day">TUE</span><span class="day">WED</span><span class="day">THUR</span><span class="day">FRI</span><span class="day">SAT</span>
      <span class="date">1</span><span class="date date--today"><i>2</i></span><span class="date">3</span><span class="date">4</span><span class="date">5</span><span class="date">6</span><span class="date">7</span>
    </div>

    <article class="task" style="top:331px">
      <div class="task__photo" role="img" aria-label="Exercise photo"></div>
      <div class="task__title">Nemo enim ipsam</div><div class="task__sub">quia voluptas sit</div>
      <div class="task__time"><svg width="12" height="12" viewBox="0 0 12 12"><circle cx="6" cy="6" r="4.8" fill="none" stroke="#0cb31a" stroke-width="1.8"/><path d="M6 3.5V6h2" fill="none" stroke="#0cb31a" stroke-width="1.5"/></svg>10 min</div>
      <svg class="task__go" width="20" height="20" viewBox="0 0 20 20"><circle cx="10" cy="10" r="9" fill="none" stroke="#555" stroke-width="1.2"/><path d="m8 6 4 4-4 4" fill="none" stroke="#555" stroke-width="1.4"/></svg>
    </article>
    <article class="task" style="top:430px">
      <div class="task__photo" role="img" aria-label="Exercise photo"></div>
      <div class="task__title">Nemo enim ipsam</div><div class="task__sub">quia voluptas sit</div>
      <div class="task__time"><svg width="12" height="12" viewBox="0 0 12 12"><circle cx="6" cy="6" r="4.8" fill="none" stroke="#0cb31a" stroke-width="1.8"/><path d="M6 3.5V6h2" fill="none" stroke="#0cb31a" stroke-width="1.5"/></svg>10 min</div>
      <svg class="task__go" width="20" height="20" viewBox="0 0 20 20"><circle cx="10" cy="10" r="9" fill="none" stroke="#555" stroke-width="1.2"/><path d="m8 6 4 4-4 4" fill="none" stroke="#555" stroke-width="1.4"/></svg>
    </article>
    <article class="task" style="top:529px">
      <div class="task__photo" role="img" aria-label="Exercise photo"></div>
      <div class="task__title">Nemo enim ipsam</div><div class="task__sub">quia voluptas sit</div>
      <div class="task__time"><svg width="12" height="12" viewBox="0 0 12 12"><circle cx="6" cy="6" r="4.8" fill="none" stroke="#0cb31a" stroke-width="1.8"/><path d="M6 3.5V6h2" fill="none" stroke="#0cb31a" stroke-width="1.5"/></svg>10 min</div>
      <svg class="task__go" width="20" height="20" viewBox="0 0 20 20"><circle cx="10" cy="10" r="9" fill="none" stroke="#555" stroke-width="1.2"/><path d="m8 6 4 4-4 4" fill="none" stroke="#555" stroke-width="1.4"/></svg>
    </article>
    <article class="task" style="top:627px">
      <div class="task__photo" role="img" aria-label="Exercise photo"></div>
      <div class="task__title">Nemo enim ipsam</div><div class="task__sub">quia voluptas sit</div>
      <div class="task__time"><svg width="12" height="12" viewBox="0 0 12 12"><circle cx="6" cy="6" r="4.8" fill="none" stroke="#0cb31a" stroke-width="1.8"/><path d="M6 3.5V6h2" fill="none" stroke="#0cb31a" stroke-width="1.5"/></svg>10 min</div>
      <svg class="task__go" width="20" height="20" viewBox="0 0 20 20"><circle cx="10" cy="10" r="9" fill="none" stroke="#555" stroke-width="1.2"/><path d="m8 6 4 4-4 4" fill="none" stroke="#555" stroke-width="1.4"/></svg>
    </article>
    <article class="task" style="top:726px">
      <div class="task__photo" role="img" aria-label="Exercise photo"></div>
      <div class="task__title">Nemo enim ipsam</div><div class="task__sub">quia voluptas sit</div>
      <div class="task__time"><svg width="12" height="12" viewBox="0 0 12 12"><circle cx="6" cy="6" r="4.8" fill="none" stroke="#0cb31a" stroke-width="1.8"/><path d="M6 3.5V6h2" fill="none" stroke="#0cb31a" stroke-width="1.5"/></svg>10 min</div>
      <svg class="task__go" width="20" height="20" viewBox="0 0 20 20"><circle cx="10" cy="10" r="9" fill="none" stroke="#555" stroke-width="1.2"/><path d="m8 6 4 4-4 4" fill="none" stroke="#555" stroke-width="1.4"/></svg>
    </article>
  </section>

  <!-- Testimonials screen -->
  <section class="screen screen--reviews">
    <header class="topbar">
      <span class="topbar__back"><svg width="22" height="20" viewBox="0 0 22 20"><path d="M10 2 2 10l8 8M2 10h18" fill="none" stroke="#fff" stroke-width="4" stroke-linecap="round" stroke-linejoin="round"/></svg></span>
      <h1 class="topbar__title">Testimonials</h1>
      <span class="topbar__search"><svg width="20" height="20" viewBox="0 0 20 20"><circle cx="8" cy="8" r="6" fill="none" stroke="#fff" stroke-width="3"/><path d="m12.5 12.5 5 5" stroke="#fff" stroke-width="3.4" stroke-linecap="round"/></svg></span>
    </header>
    <div class="brand-name">BendTheRoutine</div>

    <article class="review" style="top:186px">
      <div class="review__photo" role="img" aria-label="Reviewer portrait"></div>
      <div class="review__head"><span class="review__quote">“</span><span class="review__name">John Doe</span><span class="review__stars"><svg width="72" height="13" viewBox="0 0 72 13"><g fill="#f5a623"><path id="st" d="M6.5 0 8.2 4.4 13 4.7 9.3 7.7 10.5 12.4 6.5 9.8 2.5 12.4 3.7 7.7 0 4.7 4.8 4.4z"/><use href="#st" x="14.5"/><use href="#st" x="29"/><use href="#st" x="43.5"/><use href="#st" x="58"/></g></svg></span></div>
      <p class="review__text">Sed ut perspiciatis unde omnis iste natus error sit voluptatem accusantium doloremque lauium, totam rem aperiam, eaque ipsa quae ab illo inventore</p>
    </article>
    <article class="review" style="top:366px">
      <div class="review__photo" role="img" aria-label="Reviewer portrait"></div>
      <div class="review__head"><span class="review__quote">“</span><span class="review__name">John Doe</span><span class="review__stars"><svg width="72" height="13" viewBox="0 0 72 13"><g fill="#f5a623"><use href="#st"/><use href="#st" x="14.5"/><use href="#st" x="29"/><use href="#st" x="43.5"/><use href="#st" x="58"/></g></svg></span></div>
      <p class="review__text">Sed ut perspiciatis unde omnis iste natus error sit voluptatem accusantium doloremque lauium, totam rem aperiam, eaque ipsa quae ab illo inventore</p>
    </article>
    <article class="review" style="top:546px">
      <div class="review__photo" role="img" aria-label="Reviewer portrait"></div>
      <div class="review__head"><span class="review__quote">“</span><span class="review__name">John Doe</span><span class="review__stars"><svg width="72" height="13" viewBox="0 0 72 13"><g fill="#f5a623"><use href="#st"/><use href="#st" x="14.5"/><use href="#st" x="29"/><use href="#st" x="43.5"/><use href="#st" x="58"/></g></svg></span></div>
      <p class="review__text">Sed ut perspiciatis unde omnis iste natus error sit voluptatem accusantium doloremque lauium, totam rem aperiam, eaque ipsa quae ab illo inventore</p>
    </article>
    <div class="more-reviews">VIEW MORE REVIEWS</div>
  </section>

  <!-- Social media screen -->
  <section class="screen screen--social">
    <header class="topbar">
      <span class="topbar__back"><svg width="22" height="20" viewBox="0 0 22 20"><path d="M10 2 2 10l8 8M2 10h18" fill="none" stroke="#fff" stroke-width="4" stroke-linecap="round" stroke-linejoin="round"/></svg>Back</span>
      <h1 class="topbar__title">Social Media</h1>
      <span class="topbar__search"><svg width="20" height="20" viewBox="0 0 20 20"><circle cx="8" cy="8" r="6" fill="none" stroke="#fff" stroke-width="3"/><path d="m12.5 12.5 5 5" stroke="#fff" stroke-width="3.4" stroke-linecap="round"/></svg></span>
    </header>
    <a class="network" style="left:23px;top:98px"><span class="network__dot"></span><span class="network__name">Snapgrove</span></a>
    <a class="network" style="left:193px;top:98px"><span class="network__dot"></span><span class="network__name">ChirpLine</span></a>

    <div class="feed">
      <div class="post" style="top:0;height:119px">
        <div class="post__avatar" role="img" aria-label="Member portrait" style="left:252px;top:20px"></div>
        <div class="post__name" style="left:22px;top:30px">John Doe</div>
        <div class="post__text" style="left:23px;top:58px">Lorem ipsum dolor sit amet,<br>consectetur adipiscing elit, sed</div>
      </div>
      <div class="post" style="top:119px;height:101px">
        <div class="post__avatar" role="img" aria-label="Member portrait" style="left:13px;top:19px"></div>
        <div class="post__name" style="left:90px;top:28px">Manuel</div>
        <div class="post__text" style="left:90px;top:49px">Nemo enim ipsam voluptate</div>
      </div>
      <div class="post" style="top:220px;height:105px">
        <div class="post__avatar" role="img" aria-label="Member portrait" style="left:252px;top:9px"></div>
        <div class="post__name" style="left:22px;top:18px">John Doe</div>
        <div class="post__text" style="left:23px;top:46px">Lorem ipsum dolor sit amet,<br>consectetur adipiscing elit, sed</div>
      </div>
      <a class="feed__more">View More</a>
    </div>

    <a class="network" style="left:23px;top:658px"><span class="network__dot"></span><span class="network__name">Boardnook</span></a>
    <a class="network" style="left:193px;top:658px"><span class="network__dot"></span><span class="network__name">Meetwall</span></a>
  </section>

</div>
</body>
</html>
```